Business Card Design for a Software Startup

We'd like to have a business card design. We already have a logo. Basically what we need is a clean design with name, address, cellphone and phone numbers, e-mail and web site address (front) and a space on the back with our logo with the company name on the right side and some texts on the bottom.
We are a development and consulting company in Brazil with highly qualified team of professionals in Java, iOS and Android development and consulting.

Target Market(s)

CIO, IT managers of mid to big size companies

Industry/Entity Type

Business

```html
<!DOCTYPE html>
<html lang="en">
<head>
<meta charset="utf-8">
<title>NORVEX Business Card</title>
<link href="https://fonts.googleapis.com/css2?family=Mulish:wght@400;600;800&display=swap" rel="stylesheet">
<style>
  :root {
    --canvas: #e9ecef;
    --paper: #fbfbfa;
    --navy: #1f3a66;
    --ink: #33465f;
    --blue: #1b7fc3;
    --blue-deep: #0f5f9e;
    --blue-light: #2b98d8;
    --rule: #b9c0c8;
    --white: #ffffff;
  }
  * { margin: 0; padding: 0; box-sizing: border-box; }
  html, body {
    width: 1200px; height: 800px; overflow: hidden;
    background: var(--canvas);
    font-family: "Mulish", sans-serif;
  }
  .canvas { position: relative; width: 1200px; height: 800px; }

  .card {
    position: absolute; top: 252px;
    width: 520px; height: 297px;
    box-shadow: 0 6px 20px rgba(20, 40, 70, 0.18);
    overflow: hidden;
  }

  /* Front */
  .card-front { left: 60px; background: var(--paper); }
  .edge-tab {
    position: absolute; left: 0; top: 98px;
    width: 10px; height: 32px; background: var(--blue);
  }
  .brand {
    position: absolute; right: 40px; top: 38px;
    display: flex; align-items: center; gap: 10px;
  }
  .brand-square { width: 40px; height: 40px; background: var(--blue); border-radius: 5px; }
  .brand-name {
    font-weight: 800; font-size: 44px; line-height: 1;
    color: var(--navy); letter-spacing: 0.5px;
  }
  .holder {
    position: absolute; left: 36px; bottom: 40px; text-align: right;
    white-space: nowrap;
  }
  .holder-name { font-weight: 800; font-size: 17px; color: var(--navy); letter-spacing: 0.3px; }
  .holder-role { font-size: 14px; color: var(--ink); }
  .address {
    position: absolute; left: 206px; bottom: 66px;
    font-size: 13px; line-height: 1.35; color: var(--ink);
    font-style: normal; white-space: nowrap;
  }
  .divider {
    position: absolute; left: 334px; bottom: 70px;
    width: 1px; height: 36px; background: var(--rule);
  }
  .contacts {
    position: absolute; left: 346px; bottom: 70px;
    font-size: 12.5px; line-height: 1.45; color: var(--ink);
    list-style: none; white-space: nowrap;
  }
  .contacts li { display: flex; align-items: center; gap: 6px; }
  .contacts svg { width: 12px; height: 12px; flex: none; }

  /* Back */
  .card-back {
    left: 620px;
    background: linear-gradient(115deg, var(--blue-light) 0%, var(--blue) 45%, var(--blue-deep) 100%);
    display: flex; align-items: center; justify-content: center;
  }
  .card-back .brand { position: static; gap: 14px; }
  .card-back .brand-square { background: var(--white); width: 46px; height: 46px; }
  .card-back .brand-name { color: var(--white); font-size: 50px; }
</style>
</head>
<body>
<main class="canvas">
  <section class="card card-front" aria-label="Business card front">
    <div class="edge-tab"></div>
    <div class="brand">
      <div class="brand-square"></div>
      <span class="brand-name">NORVEX</span>
    </div>
    <div class="holder">
      <div class="holder-name">CAIO MENDES</div>
      <div class="holder-role">Manager</div>
    </div>
    <address class="address">
      Rua das Palmeiras<br>Centro - Campinas
    </address>
    <div class="divider"></div>
    <ul class="contacts">
      <li>
        <svg viewBox="0 0 12 12" aria-hidden="true"><rect x="3" y="0.5" width="6" height="11" rx="1.2" fill="none" stroke="#1b7fc3" stroke-width="1.1"/><line x1="5" y1="9.5" x2="7" y2="9.5" stroke="#1b7fc3" stroke-width="1"/></svg>
        +55 19 4000 5821
      </li>
      <li>
        <svg viewBox="0 0 12 12" aria-hidden="true"><rect x="0.5" y="2.5" width="11" height="7.5" fill="#1b7fc3"/><polyline points="0.8,2.8 6,7 11.2,2.8" fill="none" stroke="#fbfbfa" stroke-width="1"/></svg>
        contato@norvexit.com
      </li>
    </ul>
  </section>

  <section class="card card-back" aria-label="Business card back">
    <div class="brand">
      <div class="brand-square"></div>
      <span class="brand-name">NORVEX</span>
    </div>
  </section>
</main>
</body>
</html>
```